Investment website design - investing in mutual funds

I need a design of a website (only homepage for now) dedicated to investment in mutual funds. Attached is a mock up with all the elements the homepage design should contain. The homepage should contain a logo in the upper left corner, the domain the website will run on is www.perovalstrinka.cz , in the upper right corner there should be 2 buttons or links SIGN UP / SIGN IN. The bottom of the homepage should contain links to ABOUT US, FAQ, PRIVACY POLICY, CONTACT US.
Now the main elements on the homepage
1) Video that will explain how the investment works exactly, under this video we will have 3 illustrated icons like the ones attached (see 2nd attachement) that will show the potential investor what exactly they could get when investing with us (education for kids, happy life after they retire, regular monthly payment for the rest of their life).
2) On the right side next to the video we will have a calculator where a potential investor can play with the numbers, the investor can fill in the MONTHLY PAYMENT that he wants to invest regularly every month, the time frame of the investment - for how long he wants to invest. Once the potential investor selects those 2 variables we will calculate for him 2 options - either he can get a ONE TIME PAYOUT once he reaches his investment horizon or he can get a regular monthly payment for the rest of his life. Under the laculator there will be a button 'I want to invest ->'. The functionality of the calculator should be similar to the calculator that can be found here http://www.brodavbank.cz/brodav-podilove-fondy/ and https://felbo.cz/.
The design should look similar to https://felbo.cz/ (font, colors, logo). We prefer white background in the area where we have the video and calculator. We also like the design of www.tarvupo.com. Let me know if you have any questions.

```html
<!DOCTYPE html>
<html lang="en">
<head>
<meta charset="utf-8">
<title>Perova Strinka – Mutual Fund Investing</title>
<link rel="stylesheet" href="https://fonts.googleapis.com/css2?family=Poppins:wght@400;500;600;700&family=Open+Sans:wght@400;600&display=swap">
<style>
:root{
  --brand:#0aa0dc;
  --ink:#2b2b2b;
  --muted:#555;
  --panel:#f2f2f2;
  --line:#dcdcdc;
  --header-bg:#f8f8f8;
  --white:#fff;
}
*{box-sizing:border-box;margin:0;padding:0}
html,body{width:1200px;height:885px;overflow:hidden;background:var(--white);font-family:"Poppins",sans-serif;color:var(--ink)}
.page{position:relative;width:1200px;height:885px}
.site-header{position:absolute;left:0;top:0;width:1200px;height:88px;background:var(--header-bg);border-bottom:1px solid var(--line)}
.brand-name{position:absolute;left:97px;top:20px;font-size:35px;font-weight:700;letter-spacing:.5px;color:var(--ink)}
.auth-btn{position:absolute;top:28px;height:29px;width:80px;border:2px solid var(--brand);border-radius:3px;font-size:15px;font-weight:500;display:flex;align-items:center;justify-content:center;text-decoration:none}
.auth-btn.sign-in{left:933px;background:var(--brand);color:var(--white)}
.auth-btn.sign-up{left:1020px;background:var(--white);color:var(--brand)}
.section-title{position:absolute;top:136px;font-size:26px;font-weight:400;color:var(--ink)}
.video-title{left:98px}
.calc-title{left:620px}
.video{position:absolute;left:99px;top:203px;width:497px;height:291px;background:linear-gradient(180deg,#1d6d96 0%,#2a8fb8 55%,#4bbfd8 100%)}
.play-btn{position:absolute;left:215px;top:128px;width:65px;height:37px;background:#1e1e1e;border-radius:4px}
.play-btn svg{position:absolute;left:26px;top:11px}
.controls{position:absolute;left:17px;top:252px;width:462px;height:30px;background:rgba(20,20,20,.85);border-radius:4px}
.progress{position:absolute;left:8px;top:10px;width:368px;height:9px;border:1px solid #aaa;background:#333}
.progress span{display:block;width:250px;height:100%;background:#f5d90a}
.time-tip{position:absolute;left:184px;top:-9px;font-size:9px;background:#fff;color:#000;padding:0 3px;font-family:"Open Sans",sans-serif}
.hd{position:absolute;left:420px;top:7px;font-size:12px;font-weight:700;font-style:italic;color:var(--brand)}
.benefits{position:absolute;left:98px;top:529px;width:500px;height:140px}
.benefit{position:absolute;top:0;text-align:center;width:160px}
.benefit .art{width:109px;height:109px;border-radius:50%;margin:0 auto}
.benefit .label{margin-top:12px;font-size:16px;font-weight:500;color:var(--ink)}
.b1{left:-11px}.b1 .art{background:radial-gradient(circle,#ffe04a,#f5c400)}
.b2{left:168px}.b2 .art{background:radial-gradient(circle,#3a8fd0,#1b6fb3)}
.b3{left:342px}.b3 .art{background:radial-gradient(circle,#f8c257,#f2a83a)}
.calculator{position:absolute;left:624px;top:203px;width:476px;height:466px;background:var(--panel);border:1px solid var(--line)}
.field{position:absolute;left:25px;width:427px;height:38px;background:var(--white);border:1px solid #cfcfcf;border-radius:2px;font-family:"Open Sans",sans-serif;font-size:11px;color:var(--muted);padding:0 11px;display:flex;align-items:center}
.f1{top:32px}.f2{top:182px}.f3{top:268px}
.length-label{position:absolute;left:25px;top:96px;font-size:14px;color:var(--ink)}
.slider{position:absolute;left:25px;top:132px;width:427px;height:5px;background:#aaa;border-radius:3px}
.slider .fill{width:114px;height:100%;background:var(--brand);border-radius:3px}
.slider .knob{position:absolute;left:105px;top:-7px;width:18px;height:18px;border-radius:50%;background:var(--brand)}
.range-min,.range-max{position:absolute;top:149px;font-family:"Open Sans",sans-serif;font-size:11px;color:var(--ink)}
.range-min{left:25px}.range-max{right:25px}
.or{position:absolute;left:0;width:100%;top:236px;text-align:center;font-family:"Open Sans",sans-serif;font-size:14px;color:var(--ink)}
.invest-btn{position:absolute;left:25px;top:334px;width:190px;height:41px;background:var(--brand);border-radius:2px;color:var(--white);font-size:15px;font-weight:600;letter-spacing:.5px;display:flex;align-items:center;justify-content:center}
.site-footer{position:absolute;left:0;top:742px;width:1200px;height:143px;background:var(--panel);border-top:1px solid var(--line);font-family:"Open Sans",sans-serif;text-align:center;color:var(--ink)}
.footer-nav{margin-top:50px;font-size:12.5px}
.footer-nav a{color:var(--ink);text-decoration:none}
.footer-nav .sep{margin:0 10px}
.copyright{margin-top:17px;font-size:12.5px}
</style>
</head>
<body>
<div class="page">
  <header class="site-header">
    <div class="brand-name">Perova Strinka</div>
    <a class="auth-btn sign-in" href="#">Sign in</a>
    <a class="auth-btn sign-up" href="#">Sign up</a>
  </header>

  <h2 class="section-title video-title">Video About Our Product</h2>
  <h2 class="section-title calc-title">Our Online Calculator</h2>

  <div class="video">
    <div role="img" aria-label="Illustration of a businessman with a telescope looking at a rising growth chart over a city skyline" style="position:absolute;inset:0"></div>
    <div class="play-btn"><svg width="14" height="15" viewBox="0 0 14 15"><path d="M0 0L14 7.5L0 15Z" fill="#fff"/></svg></div>
    <div class="controls">
      <div class="progress"><span></span></div>
      <div class="time-tip">00:34</div>
      <div class="hd">HD</div>
    </div>
  </div>

  <div class="benefits">
    <div class="benefit b1"><div class="art" role="img" aria-label="Illustration of a child reading a book"></div><div class="label">Education for kids</div></div>
    <div class="benefit b2"><div class="art" role="img" aria-label="Illustration of a hand holding a potted money plant"></div><div class="label">Passive income</div></div>
    <div class="benefit b3"><div class="art" role="img" aria-label="Illustration of a cheerful retired couple"></div><div class="label">Happy Retirement</div></div>
  </div>

  <section class="calculator">
    <div class="field f1">Regular monthly investment:</div>
    <div class="length-label">Length of investment:</div>
    <div class="slider"><div class="fill"></div><div class="knob"></div></div>
    <div class="range-min">0</div>
    <div class="range-max">30 years</div>
    <div class="field f2">One time payout:</div>
    <div class="or">OR</div>
    <div class="field f3">Monthly payment:</div>
    <div class="invest-btn">I WANT TO INVEST &rsaquo;</div>
  </section>

  <footer class="site-footer">
    <nav class="footer-nav">
      <a href="#">ABOUT US</a><span class="sep">|</span><a href="#">FAQ</a><span class="sep">|</span><a href="#">PRIVACY POLICY</a><span class="sep">|</span><a href="#">CONTACT</a>
    </nav>
    <p class="copyright">Copyright © 2017 Perova Strinka. All Rights Reserved.</p>
  </footer>
</div>
</body>
</html>
```